New Business Card for Casual Beachfront Cafe

Quirky Beachfront Cafe at Moana, South Australia needs a DOUBLE SIDED business card to print on PrintHarbor.

Target Market(s)

Business Cards sit on the counter for Guests to take with them. Please view our website www.saltreefcafe.com.au to get a feel for the Cafe. You may also view our Instagram at @saltreefcafe

Industry/Entity Type

Cafe / Restaurant

Contact Information for Business Card

Information equivalent to: Breakfast, Lunch, Dinner, Coffee, Takeaway / 117 Parade Wavecrest QX 0999 / Menu & Opening Hours: www.saltreefcafe.com.au / ph (08) 8461 9273

Requirements
Must have
• Information equivalent to: Breakfast, Lunch, Dinner, Coffee, Takeaway / 117 Parade Wavecrest QX 0999 / Menu & Opening Hours: www.saltreefcafe.com.au / ph (08) 8461 9273
Nice to have
• Potentially some of our trademark colours (Cafe can be searched via Seekly)
Should not have
• Must NOT have image of the building. May have the logo provided on one side but not necessarily, depending on how you wish to design the card

```html
<!DOCTYPE html>
<html lang="en">
<head>
<meta charset="utf-8">
<title>Salt Reef Cafe – Business Card</title>
<link rel="stylesheet" href="https://fonts.googleapis.com/css2?family=Lato:ital,wght@0,300;0,900;1,700&display=swap">
<style>
  :root {
    --rust: #b25628;
    --navy: #164a80;
    --sun: #f2e60c;
    --paper: #ffffff;
    --backdrop: #d6d6d6;
  }
  html, body {
    margin: 0;
    width: 1200px;
    height: 1200px;
    overflow: hidden;
    background: var(--backdrop);
    font-family: "Lato", sans-serif;
  }
  .card {
    position: absolute;
    left: 190px;
    width: 819px;
    height: 479px;
    display: block;
  }
  .card--front { top: 89px; }
  .card--back { top: 631px; }
  .tagline {
    font-family: "Lato", sans-serif;
    font-style: italic;
    font-weight: 700;
    font-size: 22px;
    fill: var(--paper);
  }
  .contact {
    font-family: "Lato", sans-serif;
    font-weight: 300;
    font-size: 15.5px;
    fill: var(--paper);
  }
  .brand-name {
    font-family: "Lato", sans-serif;
    font-weight: 900;
    fill: var(--navy);
  }
  .brand-name--top { font-size: 40px; }
  .brand-name--bottom { font-size: 52px; }
  .icon { fill: none; stroke: var(--paper); stroke-width: 1.3; }
</style>
</head>
<body>

<svg class="card card--front" viewBox="0 0 655 383" aria-label="Business card front">
  <rect class="card-base" width="655" height="383" fill="var(--paper)"/>
  <polygon class="wedge wedge--rust" points="0,0 270,132 270,249 0,383" fill="var(--rust)"/>
  <polygon class="wedge wedge--navy" points="270,132 655,0 655,383 270,249" fill="var(--navy)"/>

  <g class="brand-block">
    <rect x="45" y="137" width="220" height="110" fill="var(--sun)"/>
    <text class="brand-name brand-name--top" x="155" y="187" text-anchor="middle" textLength="200" lengthAdjust="spacingAndGlyphs">SALT REEF</text>
    <text class="brand-name brand-name--bottom" x="155" y="235" text-anchor="middle" textLength="128" lengthAdjust="spacingAndGlyphs">CAFE</text>
  </g>

  <g class="services">
    <text class="tagline" x="613" y="137" text-anchor="end">Breakfast, Lunch, Dinner,</text>
    <text class="tagline" x="613" y="167" text-anchor="end">Coffee, Takeaway</text>
  </g>

  <g class="contact-list">
    <text class="contact" x="592" y="213" text-anchor="end">(08) 8461 9273</text>
    <text class="contact" x="592" y="238" text-anchor="end">www.saltreefcafe.com.au</text>
    <text class="contact" x="592" y="263" text-anchor="end">117 Parade Wavecrest QX 0999</text>
    <text class="contact" x="592" y="300" text-anchor="end">@saltreefcafe</text>
  </g>

  <g class="contact-icons">
    <path class="icon icon--phone" d="M603 203 q0 8 8 8 l1.5 -2 -2.5 -2 -1.5 1.5 q-2.5 -1 -3.5 -3.5 l1.5 -1.5 -2 -2.5 z"/>
    <g class="icon icon--web">
      <circle cx="607" cy="233" r="5"/>
      <path d="M602 233 h10 M607 228 q-3 5 0 10 q3 -5 0 -10"/>
    </g>
    <g class="icon icon--pin">
      <path d="M607 264 q-4 -4 -4 -7 a4 4 0 0 1 8 0 q0 3 -4 7 z"/>
      <path d="M602 267 h10"/>
    </g>
    <rect class="icon icon--social" x="602.5" y="290" width="9" height="9" rx="2.5"/>
  </g>
</svg>

<svg class="card card--back" viewBox="0 0 655 383" aria-label="Business card back">
  <rect class="card-base" width="655" height="383" fill="var(--rust)"/>
  <polygon class="photo-area" role="img" aria-label="Yellow-toned photo of the beachfront cafe terrace" points="18,18 638,363 18,363" fill="var(--sun)"/>
  <polygon class="stripe stripe--navy" points="18,18 98,18 638,320 638,363" fill="var(--navy)"/>
  <polygon class="stripe stripe--white" points="210,18 288,18 638,214 638,257" fill="var(--paper)"/>
  <polygon class="stripe stripe--navy" points="356,18 433,18 638,133 638,176" fill="var(--navy)"/>
  <polygon class="stripe stripe--white" points="503,18 580,18 638,50 638,93" fill="var(--paper)"/>

  <g class="brand-block">
    <text class="brand-name brand-name--top" x="172" y="283" text-anchor="middle" textLength="202" lengthAdjust="spacingAndGlyphs">SALT REEF</text>
    <text class="brand-name brand-name--bottom" x="172" y="328" text-anchor="middle" textLength="128" lengthAdjust="spacingAndGlyphs">CAFE</text>
  </g>
</svg>

</body>
</html>
```